Personal Care and Home care ingredients Brochure

We need a flyer or brochure of the of chemicals we distribute for the manufacturing of personal care products such as shampoos, liquid soaps, creams, lotions, conditioners, hand sanitizer, Hair Jellys, etc and for Home care products such as, liquid soaps, desinfectants, cleaners, stain removers,etc.
The idea is to send this pdf brochure via email and companies feel very confortable with the impression it gives. We want to call attention.
Target Market(s)
Companies that manufactures cosmetics, personal care products and home care products.
Colors
Designer to choose colors to be used in the design.
Requirements
Must have
- Images that refers to the skin, hair, cleaning, washing

```html
<!DOCTYPE html>
<html lang="es">
<head>
<meta charset="utf-8">
<title>VERDAFONATE – Ficha de producto</title>
<link href="https://fonts.googleapis.com/css2?family=Didact+Gothic&family=Questrial&display=swap" rel="stylesheet">
<style>
:root{
  --bg:#e6e4e1;
  --paper:#ffffff;
  --green:#97c95a;
  --green-dark:#7db43d;
  --teal:#2f9a86;
  --sky:#a9dbe7;
  --ink:#1d1d1d;
  --muted:#5a5a5a;
  --rule:#b9b9b9;
}
*{box-sizing:border-box;margin:0;padding:0}
html,body{width:1200px;height:776px;overflow:hidden;background:var(--bg)}
body{position:relative;font-family:"Didact Gothic",sans-serif;color:var(--ink)}
.page{position:absolute;top:55px;width:494px;height:637px;background:var(--paper);box-shadow:0 3px 10px rgba(0,0,0,.25);overflow:hidden}
.page--front{left:75px}
.page--back{left:625px}
.hero{position:absolute;left:0;top:0;width:494px;height:275px}
.brand{position:absolute;left:20px;top:62px;display:flex;align-items:center;gap:7px;font-family:"Questrial",sans-serif;font-size:22px;letter-spacing:1px;color:var(--ink)}
.brand__mark{width:14px;height:14px;background:var(--teal)}
.title{position:absolute;left:14px;font-family:"Questrial",sans-serif;font-weight:400;font-size:16px;line-height:19px;color:var(--ink)}
.intro{position:absolute;left:14px;top:333px;width:466px;font-size:8.8px;line-height:11.6px;color:var(--muted);text-align:justify}
.col{position:absolute;top:400px;font-size:9px;color:var(--muted)}
.col h3{font-family:"Questrial",sans-serif;font-weight:400;font-size:9.4px;color:var(--ink);margin-bottom:4px}
.col--left{left:16px;width:225px}
.col--right{left:260px;width:222px;text-align:justify;line-height:12.8px}
.col-divider{position:absolute;left:247px;top:398px;width:1px;height:86px;background:var(--rule)}
.checks{list-style:none}
.checks li{position:relative;padding-left:14px;line-height:12.9px}
.checks li::before{content:"";position:absolute;left:1px;top:3px;width:7px;height:7px;border:1px solid var(--green-dark);border-radius:50%}
.features{position:absolute;left:10px;top:489px;width:474px;display:flex;justify-content:space-between}
.feature{width:118px;text-align:center;font-size:8.2px;line-height:10px;color:var(--muted)}
.feature svg{display:block;margin:0 auto 11px}
.feature b{display:block;font-family:"Questrial",sans-serif;font-weight:400;font-size:8.6px;line-height:10.5px;color:var(--ink)}
.footer{position:absolute;left:0;bottom:0;width:494px;height:19px;background:var(--teal);color:#fff;font-size:9.5px;letter-spacing:1px;text-align:center;line-height:19px}
.diagram{position:absolute;left:0;top:0;width:494px;height:300px}
.pill{position:absolute;background:var(--green);color:#fff;text-align:center;border-radius:12px}
.pill--main{left:186px;top:261px;width:120px;height:22px;font-family:"Questrial",sans-serif;font-size:18px;line-height:22px;border-radius:12px}
.pill--sub{top:294px;height:17px;font-size:8px;line-height:17px}
.box{position:absolute;top:304px;height:102px;border:1px solid var(--green);border-radius:9px;padding:16px 9px 0;font-size:7.3px;line-height:9.4px;color:var(--muted)}
.box h4{font-weight:400;font-size:7.8px;line-height:10.5px;color:var(--ink);margin-bottom:2px}
.box--left{left:17px;width:219px}
.box--right{left:255px;width:219px}
.notes{position:absolute;left:17px;top:421px;width:460px;font-size:8.8px;line-height:12.8px;color:var(--muted)}
.recs{position:absolute;left:17px;top:503px;width:457px;height:101px;background:var(--green);border-radius:10px;color:#fff;font-size:7.8px;line-height:10.4px}
.recs__tab{position:absolute;left:122px;top:-11px;width:214px;height:22px;background:#fff;border:1px solid var(--green);border-radius:11px;color:var(--ink);font-family:"Questrial",sans-serif;font-size:9.2px;text-align:center;line-height:20px}
.recs__grid{position:absolute;left:8px;top:18px;width:442px;display:grid;grid-template-columns:1fr 1fr;column-gap:12px;row-gap:6px}
.recs__grid li{line-height:10.4px}
.recs .checks li::before{border-color:#fff}
</style>
</head>
<body>

<section class="page page--front">
  <svg class="hero" viewBox="0 0 494 275" role="img" aria-label="Foto de familia tendiendo ropa blanca y una camiseta a rayas rosas al aire libre">
    <defs>
      <linearGradient id="laundryOutdoor" x1="0" y1="0" x2="1" y2="1">
        <stop offset="0" stop-color="#7f9a5a"/>
        <stop offset=".45" stop-color="#d9ddd4"/>
        <stop offset=".7" stop-color="#e98aa2"/>
        <stop offset="1" stop-color="#b9c7a4"/>
      </linearGradient>
    </defs>
    <path d="M0,120 C90,110 190,65 240,0 L494,0 L494,220 C380,238 250,244 150,256 C90,262 40,262 0,260 Z" fill="url(#laundryOutdoor)"/>
    <path d="M0,120 C90,110 190,65 240,0" fill="none" stroke="var(--sky)" stroke-width="9"/>
    <path d="M0,258 C90,255 200,246 300,234 C400,222 460,212 494,205" fill="none" stroke="var(--green)" stroke-width="9"/>
    <path d="M0,272 C120,266 260,256 360,243 C430,234 470,226 494,220" fill="none" stroke="var(--sky)" stroke-width="8"/>
    <path d="M0,275 L0,268 C120,263 260,253 360,244 C430,236 470,229 494,224 L494,275 Z" fill="var(--paper)"/>
  </svg>
  <div class="brand"><span class="brand__mark"></span>NOVAQUIM</div>

  <h1 class="title" style="top:293px">Nueva linea de VERDAFONATE<br>Sulfonatos de Ester Metilico (MES)</h1>
  <p class="intro">El VERDAFONATE es un surfactante ionico utilizado como ingrediente activo en detergentes. Su principal uso es como substituto del surfactante universalmente utilizado, LAS o alquil sulfonatos lineales en las formulas de los detergentes. Esta hecho de recursos naturales renovables, lo cual le da un excelente biodegradabilidad, y muestra una mejor detergencia y tolerancia a la dureza durante el lavado.</p>

  <div class="col col--left">
    <h3>El VERDAFONATE es un surfactante mas verde.</h3>
    <ul class="checks">
      <li>Huella mas verde</li>
      <li>Eco-amigable</li>
      <li>Hecho de fuentes renovables</li>
      <li>Sustentable</li>
      <li>Biodegradable</li>
    </ul>
  </div>
  <div class="col-divider"></div>
  <div class="col col--right">
    <h3>Versatilidad para usar en Polvos y Liquidos:</h3>
    minimixa el uso de ingredientes SKU en productos de consumo masivo. Aplicación en un amplio rango de formulaciones.
  </div>

  <div class="features">
    <div class="feature">
      <svg width="50" height="50" viewBox="0 0 52 52"><circle cx="26" cy="26" r="25" fill="var(--green)" stroke="#dfeecb" stroke-width="2"/><path d="M22,13h8v5h3v5c3,2 3,4 3,6v12H16V29c0-2 0-4 3-6v-5h3z" fill="#fff"/></svg>
      <b>EXCELENTE<br>DETERGENCIA</b>Desempeño superior en aguas con alta dureza vs las alternativa
    </div>
    <div class="feature">
      <svg width="50" height="50" viewBox="0 0 52 52"><circle cx="26" cy="26" r="25" fill="var(--green)" stroke="#dfeecb" stroke-width="2"/><path d="M26,12v5M14,24l12-7 12,7" fill="none" stroke="#fff" stroke-width="2"/><path d="M17,24h18v15H17z" fill="#fff"/></svg>
      <b>CUIDADO DE LA ROPA</b>Excelente compatibi-<br>lidad con Enzimas
    </div>
    <div class="feature">
      <svg width="50" height="50" viewBox="0 0 52 52"><circle cx="26" cy="26" r="25" fill="var(--green)" stroke="#dfeecb" stroke-width="2"/><path d="M26,12c-5,8-8,12-8,16a8,8 0 0 0 16,0c0-4-3-8-8-16z" fill="#fff"/><ellipse cx="26" cy="40" rx="11" ry="3" fill="none" stroke="#fff" stroke-width="1.5"/></svg>
      <b>VERDAFONATE</b>Seguridad y Suavidad
    </div>
    <div class="feature">
      <svg width="50" height="50" viewBox="0 0 52 52"><circle cx="26" cy="26" r="25" fill="var(--green)" stroke="#dfeecb" stroke-width="2"/><path d="M15,38C20,24 28,16 38,13 36,25 28,34 15,38z" fill="#fff"/><path d="M14,40L30,24" stroke="var(--green)" stroke-width="1.5"/></svg>
      <b>IMPARTE EL BALANCE<br>PERFECTO</b>Suave a la piel y a los textiles.
    </div>
  </div>

  <div class="footer">www.oleoverde-demo.com</div>
</section>

<section class="page page--back">
  <svg class="hero" viewBox="0 0 494 275" role="img" aria-label="Foto de madre e hija sacando ropa blanca de una lavadora">
    <defs>
      <linearGradient id="laundryRoom" x1="0" y1="0" x2="1" y2="0">
        <stop offset="0" stop-color="#d8dcdf"/>
        <stop offset=".45" stop-color="#eef0f1"/>
        <stop offset=".75" stop-color="#b58a68"/>
        <stop offset="1" stop-color="#a47652"/>
      </linearGradient>
    </defs>
    <path d="M0,0 H494 V160 C460,215 410,228 360,224 C320,221 290,212 250,202 C170,184 80,174 0,172 Z" fill="url(#laundryRoom)"/>
    <path d="M0,175 C80,177 170,187 250,205 C290,215 320,224 360,227 C410,231 460,218 494,164" fill="none" stroke="var(--sky)" stroke-width="6"/>
    <path d="M0,183 C80,185 170,195 250,213 C290,223 320,232 360,235 C410,239 460,226 494,174" fill="none" stroke="var(--green)" stroke-width="8"/>
    <path d="M0,275 V188 C80,190 170,200 250,218 C290,228 320,237 360,240 C410,244 460,231 494,180 V275 Z" fill="var(--paper)"/>
  </svg>

  <h1 class="title" style="top:212px;left:17px">VERDAFONATE<br>Sulfonatos de Ester Metilico (MES)</h1>

  <svg class="diagram" viewBox="0 0 494 300" aria-hidden="true">
    <path d="M186,272H126V296M306,272H366V296" fill="none" stroke="var(--rule)" stroke-width="1"/>
  </svg>
  <div class="pill pill--main">MES</div>

  <div class="box box--left">
    <h4>LAVAPLATOS LIQUIDOS Y DETERGENTES LIQUIDOS DE LAVANDERIA</h4>
    • Más suave para la piel<br>
    • Ingrediente Alternativo a Productos derivados<br>&nbsp;&nbsp;del Pétroleo<br>
    • Mejor detergencia en Agua Dura.<br>
    • Mejor remoción de manchas de aceite.<br>
    • Uso de productos naturales derivados de la palma.
  </div>
  <div class="pill pill--sub" style="left:35px;width:182px">REEMPLAZO DE LABSA</div>

  <div class="box box--right">
    <h4>LAVAPLATOS LIQUIDOS / DETERGENTES LIQUIDOS / JABANO DE TOCADOR LIQUIDO</h4>
    • Menor costo de materia prima por unidad activa.<br>
    • Desempeño similar<br>
    • Suavidad similar al SLES
  </div>
  <div class="pill pill--sub" style="left:274px;width:182px">REEMPLAZO DE SLES</div>

  <ul class="checks notes">
    <li>El MES no necesita neutralizacion, y al diluir la solicion ya esta activa.</li>
    <li>Se recomienda 30-50% de LABSA y no un reemplazo total para lograr un efecto - sinergistico.</li>
    <li>Comparado con el LABSA, el MES es mas suave para la piel, un tiene efecto de limpieza mas fuerte sobre manchas de grasas vegetales/oleosas y un mayor poder de detergencia en aguas con alto contenido de dureza.</li>
  </ul>

  <div class="recs">
    <div class="recs__tab">RECOMENDACIONES GENERALES</div>
    <ul class="checks recs__grid">
      <li>Si se requiero que el liquido final lavaplatos/detergente sea transparente o cristalino, el maximo contenido de MES no debe ser mas de 5%.</li>
      <li>MES no debe ser expuesto a pH menor de 5 o mayor de 9 por mas de 24 horas porque se degrada.</li>
      <li>A pesar que es posible reemplazar totalmente el LAS o LABSA, se recomienda la presencia de mas surfactantes para buscar un mejor efecto sinergistico.</li>
      <li>El uso de MES en productos liquidos requiere una dosis de ajuste de electrolito (Sal) para alcanzar la viscosidad deseada.</li>
    </ul>
  </div>

  <div class="footer">www.oleoverde-demo.com</div>
</section>

</body>
</html>
```